Glossy black background with white text, image of webcam on right.

Text:

YOU HAVE BEEN CHOSEN
to be a Camgirl online model!

- earn $10,000/month from home
- choose your own hours

Meridian Lowe
The Halvard

Dennis Pallot
Director
VELORIX PTY LTD
mob 0491 302184
email sales@velorixhq.com

www.VELORIXHQ.com

the Lowe signature can go on the back.

Meridian Lowe
The Halvard

thanks

On the front: the webcam image should be quite large

On the back: Lowe sig with an apple image or icon

good luck!

On the back should be in cursive with a small apple picture. (green)

Lowe
The Halvard

no "meridian"

Target Market(s)

young hot women

Requirements
Must have
• "You Have Been Chosen"
in the largest font
Nice to have
• see attached photo of webcam
maybe some yellow text
Should not have
• consider removing logo from webcam pic

```html
<!DOCTYPE html>
<html lang="en">
<head>
<meta charset="utf-8">
<title>Velorix business cards</title>
<link rel="stylesheet" href="https://fonts.googleapis.com/css2?family=Fjalla+One&family=Arimo:wght@400;700&family=Marcellus&display=swap">
<style>
  :root {
    --paper: #ffffff;
    --card: #000000;
    --ink: #ffffff;
    --accent-red: #e3322b;
    --cam-light: #efe6d6;
    --cam-red: #c8141b;
  }
  html, body {
    margin: 0;
    padding: 0;
    width: 1196px;
    height: 1200px;
    overflow: hidden;
    background: var(--paper);
  }
  .canvas {
    position: relative;
    width: 1196px;
    height: 1200px;
    background: var(--paper);
  }
  .card {
    position: absolute;
    left: 118px;
    width: 961px;
    background: var(--card);
    color: var(--ink);
    overflow: hidden;
  }
  .card--front { top: 52px; height: 543px; }
  .card--back { top: 606px; height: 539px; }
  .card > * { position: absolute; margin: 0; white-space: nowrap; }

  /* front */
  .front-headline {
    left: 12px; top: 6px;
    font-family: "Fjalla One", sans-serif;
    font-size: 50px; line-height: 1;
    letter-spacing: 0.5px;
  }
  .front-tagline {
    left: 12px; top: 66px;
    font-family: "Arimo", sans-serif;
    font-weight: 700;
    font-size: 25px; line-height: 1;
    color: var(--accent-red);
  }
  .contact-name {
    left: 62px; top: 182px;
    font-family: "Arimo", sans-serif;
    font-size: 46px; line-height: 1;
    letter-spacing: 5px;
  }
  .contact-role {
    left: 70px; top: 236px;
    font-family: "Arimo", sans-serif;
    font-size: 34px; line-height: 1;
  }
  .contact-line {
    left: 12px;
    font-family: "Arimo", sans-serif;
    font-size: 36px; line-height: 1;
  }
  .contact-company { top: 348px; }
  .contact-phone { top: 392px; }
  .contact-email { top: 434px; left: 18px; }
  .contact-web {
    left: 329px; top: 498px;
    font-family: "Arimo", sans-serif;
    font-size: 22px; line-height: 1;
  }
  .front-arc { left: 0; top: 0; width: 961px; height: 543px; }
  .webcam-art--front { left: 752px; top: 10px; width: 209px; height: 430px; }

  /* back */
  .back-line {
    font-family: "Marcellus", serif;
    line-height: 1;
  }
  .back-headline { left: 14px; top: 14px; font-size: 78px; letter-spacing: -1px; }
  .back-subline { left: 24px; top: 100px; font-size: 76px; letter-spacing: -1px; }
  .back-perk { left: 16px; font-size: 48px; letter-spacing: 2px; }
  .back-perk--earn { top: 196px; }
  .back-perk--hours { top: 258px; }
  .back-name { left: 6px; top: 354px; font-size: 76px; }
  .back-title { left: 10px; top: 438px; font-size: 44px; letter-spacing: 7px; }
  .webcam-art--back { left: 741px; top: 250px; width: 220px; height: 289px; }
</style>
</head>
<body>
<main class="canvas">
  <section class="card card--front" aria-label="Card front">
    <svg class="front-arc" viewBox="0 0 961 543" aria-hidden="true">
      <path d="M706 0 C 660 140, 648 330, 688 543 L 704 543 C 668 330, 680 140, 724 0 Z" fill="var(--ink)"/>
    </svg>
    <svg class="webcam-art webcam-art--front" viewBox="0 0 209 430" role="img" aria-label="Illustration of a webcam with red swooshes">
      <defs>
        <radialGradient id="camFront" cx="45%" cy="30%" r="70%">
          <stop offset="0" stop-color="var(--cam-light)" stop-opacity="0.85"/>
          <stop offset="0.45" stop-color="var(--cam-red)" stop-opacity="0.8"/>
          <stop offset="1" stop-color="var(--card)" stop-opacity="0"/>
        </radialGradient>
      </defs>
      <rect width="209" height="430" fill="url(#camFront)"/>
    </svg>
    <h1 class="front-headline">YOU HAVE BEEN CHOSEN</h1>
    <p class="front-tagline">to be a Camgirl online model!</p>
    <p class="contact-name">Dennis Pallot</p>
    <p class="contact-role">Director</p>
    <p class="contact-line contact-company">VELORIX PTY LTD</p>
    <p class="contact-line contact-phone">TEL# 0491 302184</p>
    <p class="contact-line contact-email">Email: sales@velorixhq.com</p>
    <p class="contact-web">www.VELORIXHQ.com</p>
  </section>

  <section class="card card--back" aria-label="Card back">
    <svg class="webcam-art webcam-art--back" viewBox="0 0 220 289" role="img" aria-label="Illustration of a webcam with red swooshes">
      <defs>
        <radialGradient id="camBack" cx="35%" cy="25%" r="75%">
          <stop offset="0" stop-color="var(--cam-light)" stop-opacity="0.85"/>
          <stop offset="0.45" stop-color="var(--cam-red)" stop-opacity="0.8"/>
          <stop offset="1" stop-color="var(--card)" stop-opacity="0"/>
        </radialGradient>
      </defs>
      <rect width="220" height="289" fill="url(#camBack)"/>
    </svg>
    <h2 class="back-line back-headline">YOU HAVE BEEN CHOSEN</h2>
    <p class="back-line back-subline">to be a CAMGIRL Model</p>
    <p class="back-line back-perk back-perk--earn">-earn $10,000/month from home</p>
    <p class="back-line back-perk back-perk--hours">-choose your own hours</p>
    <p class="back-line back-name">Meridian Lowe</p>
    <p class="back-line back-title">The Halvard</p>
  </section>
</main>
</body>
</html>
```